Coralbend Pastoral Traders Business Cards

We require business cards revamped with our logo. A few details we would like to use.

1. Round Edges
2. Our logo over the top of a wagyu cattle background photo on one side of the card

Other side of the card has the below details.

1. Person Name (First & Last)
2. Job Position
3. Mobile Number
4. Email Address
5. Website Address

Simple & Neat.

Target Market(s)

Sales

Industry/Entity Type

Agriculture

Contact Information for Business Card

CORALBEND PASTORAL TRADERS

Colors

Designer to choose colors to be used in the design.

Requirements
Must have
• Company Logo

```html
<!DOCTYPE html>
<html lang="en">
<head>
<meta charset="utf-8">
<title>Coralbend Pastoral Traders – Business Cards</title>
<link rel="stylesheet" href="https://fonts.googleapis.com/css2?family=Arimo:wght@400;700&display=swap">
<style>
  :root {
    --bg: #2b2b2b;
    --maroon: #660b25;
    --maroon-deep: #4e0819;
    --white: #ffffff;
    --photo-dark: #1d1512;
    --photo-mid: #4a2a1f;
    --photo-meat: #7a2a2e;
  }
  * { box-sizing: border-box; margin: 0; padding: 0; }
  html, body { width: 1200px; height: 875px; overflow: hidden; }
  body {
    background: var(--bg);
    font-family: "Arimo", Arial, sans-serif;
    position: relative;
  }
  .card {
    position: absolute;
    width: 540px;
    height: 310px;
    border-radius: 22px;
    overflow: hidden;
    box-shadow: 0 18px 40px rgba(0,0,0,.45);
  }
  .card-front { left: 60px; top: 110px; }
  .card-back { left: 600px; top: 455px; background: var(--white); }

  .photo-fill {
    position: absolute; inset: 0;
    background:
      radial-gradient(ellipse 45% 40% at 55% 55%, var(--photo-meat) 0%, var(--photo-mid) 55%, transparent 100%),
      linear-gradient(135deg, var(--photo-dark), #2e1e17 60%, var(--photo-dark));
  }
  .photo-fill::after {
    content: ""; position: absolute; inset: 0;
    background: rgba(0,0,0,.35);
  }
  .front-brand {
    position: absolute; left: 0; right: 0; top: 50%;
    transform: translateY(-50%);
    display: flex; align-items: center; justify-content: center; gap: 12px;
    color: var(--white);
  }
  .brand-dot {
    width: 18px; height: 18px; border-radius: 50%;
    background: currentColor; flex: none;
  }
  .front-brand .brand-name {
    font-weight: 700; font-size: 30px; letter-spacing: .5px;
  }

  .wave { position: absolute; inset: 0; }
  .back-brand {
    position: absolute; left: 120px; top: 70px;
    display: flex; align-items: center; gap: 10px;
    color: var(--maroon);
  }
  .back-brand .brand-name { font-weight: 700; font-size: 22px; }
  .back-brand .brand-dot { width: 14px; height: 14px; }

  .person {
    position: absolute; left: 60px; top: 228px; color: var(--white);
  }
  .person-name { font-weight: 700; font-size: 26px; letter-spacing: .5px; }
  .person-role { font-size: 15px; margin-top: 3px; }

  .divider {
    position: absolute; left: 300px; top: 190px;
    width: 1px; height: 85px; background: rgba(255,255,255,.6);
  }
  .contacts {
    position: absolute; left: 322px; top: 178px;
    list-style: none; color: var(--white); font-size: 13.5px;
  }
  .contacts li { display: flex; align-items: center; gap: 10px; height: 30px; }
  .contacts svg { width: 15px; height: 15px; flex: none; }
</style>
</head>
<body>

  <section class="card card-front" aria-label="Card front">
    <div class="photo-fill" role="img" aria-label="Photo of raw wagyu steaks on a wooden board with herbs, spices and a knife"></div>
    <div class="front-brand">
      <span class="brand-dot"></span>
      <span class="brand-name">Coralbend Pastoral Traders</span>
    </div>
  </section>

  <section class="card card-back" aria-label="Card back">
    <svg class="wave" viewBox="0 0 540 310" preserveAspectRatio="none" aria-hidden="true">
      <path d="M0,205 C120,195 210,125 330,112 C430,100 500,70 540,55 L540,310 L0,310 Z" fill="var(--maroon-deep)"/>
      <path d="M0,210 C120,200 210,130 330,117 C430,105 500,75 540,60 L540,310 L0,310 Z" fill="var(--maroon)"/>
    </svg>

    <div class="back-brand">
      <span class="brand-dot"></span>
      <span class="brand-name">Coralbend Pastoral Traders</span>
    </div>

    <div class="person">
      <p class="person-name">LIAM HARROW</p>
      <p class="person-role">Managing Director</p>
    </div>

    <span class="divider"></span>

    <ul class="contacts">
      <li>
        <svg viewBox="0 0 16 16" fill="none" stroke="currentColor" stroke-width="1.5"><rect x="4" y="1" width="8" height="14" rx="1.5"/><line x1="7" y1="12.5" x2="9" y2="12.5"/></svg>
        <span>07-5550-2184</span>
      </li>
      <li>
        <svg viewBox="0 0 16 16" fill="currentColor"><path d="M1 3h14v10H1z"/><path d="M1 3l7 6 7-6" fill="none" stroke="var(--maroon)" stroke-width="1.4"/></svg>
        <span>hello@coralbendpastoral.com</span>
      </li>
      <li>
        <svg viewBox="0 0 16 16" fill="none" stroke="currentColor" stroke-width="1.4"><circle cx="8" cy="8" r="6.5"/><ellipse cx="8" cy="8" rx="3" ry="6.5"/><line x1="1.5" y1="8" x2="14.5" y2="8"/></svg>
        <span>coralbendpastoral.com</span>
      </li>
    </ul>
  </section>

</body>
</html>
```